Energy Company 8-page Brochure

We are in need of a redesign of our 8-page brochure. Attached is the initial design that does not represent us very well. We are looking for CLEAN/CORPORATE look with a little bit of flair (graphs/charts if applicable).

I prefer white background and our company colors (blue/green) to be the accent colors. Feel free to add additional accent colors to highlight certain areas.

We are in the energy field (not just solar), so please consider the types of images that you will use. Are headquarters is located in Chicago, IL so a great looking picture of the skyline or something similar would work for the front and back cover.

We have additional marketing collateral that we will want to be uniformed once we have the right design.

Good luck, and we look forward to receiving some great designs!

Best Regards,
Rob

Target Market(s)

Small to large businesses (B2B).

Industry/Entity Type

It Company

Colors
ffffff
9bcb3c
0255a3

Requirements
Must have
• Clean design, company colors, specified content and editable files.
Nice to have
• Graphs, charts, highlighted areas where necessary.
Should not have
• Clutter! Please utilized page space appropriately. There is a lot of content, so you need to consider graphics and image placement.

```html
<!DOCTYPE html>
<html lang="en">
<head>
<meta charset="utf-8">
<title>Everything Energy – Brochure Covers</title>
<link href="https://fonts.googleapis.com/css2?family=Questrial&display=swap" rel="stylesheet">
<style>
  :root {
    --green: #9bcb3c;
    --blue: #0255a3;
    --white: #ffffff;
    --ink: #3a3a3a;
    --charcoal: #2b2b2b;
    --grey-light: #cfcfcf;
    --backdrop: #e4e4e4;
  }
  * { margin: 0; padding: 0; box-sizing: border-box; }
  html, body { width: 1200px; height: 800px; overflow: hidden; }
  body {
    background: var(--backdrop);
    font-family: "Questrial", "Century Gothic", sans-serif;
    color: var(--ink);
    position: relative;
  }
  .page {
    position: absolute;
    top: 89px;
    width: 440px;
    height: 622px;
    background: var(--white);
    box-shadow: 0 6px 18px rgba(0,0,0,.18);
    overflow: hidden;
  }
  .front-cover { left: 110px; }
  .back-cover { left: 650px; }

  /* front cover */
  .spine-bar { position: absolute; left: 18px; top: 40px; width: 12px; bottom: 0; background: var(--charcoal); }
  .spine-bar-accent { position: absolute; left: 18px; top: 350px; width: 12px; height: 110px; background: var(--green); }
  .spine-line { position: absolute; left: 36px; top: 40px; width: 3px; bottom: 0; background: var(--grey-light); }
  .side-band { position: absolute; left: 340px; top: 0; width: 26px; bottom: 0; }
  .side-band span { display: block; }
  .band-green { height: 240px; background: var(--green); }
  .band-light { height: 90px; background: linear-gradient(#e8e8e8, #bdbdbd); }
  .band-mid { height: 120px; background: linear-gradient(#9a9a9a, #6f6f6f); }
  .band-dark { height: 172px; background: linear-gradient(#4a4a4a, #222); }
  .hero-photo {
    position: absolute; left: 50px; top: 50px; width: 280px; height: 280px; border-radius: 50%;
    background: radial-gradient(circle at 55% 45%, #f3f08a 0%, #b9d94a 22%, #5e9a2e 55%, #2f5a22 100%);
  }
  .headline { position: absolute; left: 112px; top: 362px; }
  .headline-kicker { color: var(--green); font-size: 19px; letter-spacing: 1px; line-height: 1; font-weight: 400; }
  .headline-main { color: var(--ink); font-size: 46px; letter-spacing: 1px; line-height: 1; margin-top: 2px; font-weight: 400; }
  .benefit-list { position: absolute; left: 112px; top: 432px; list-style: none; }
  .benefit-list li { display: flex; align-items: center; gap: 6px; font-size: 12.5px; line-height: 21px; }
  .benefit-list svg { width: 12px; height: 12px; flex: none; }
  .partner-name-front {
    position: absolute; left: 228px; top: 556px; width: 104px;
    color: var(--green); font-size: 13px; line-height: 1.1;
  }
  .brand-front {
    position: absolute; left: 52px; bottom: 22px; display: flex; align-items: center; gap: 8px;
    color: var(--blue); font-size: 15px; line-height: 1.05;
  }
  .brand-dot { width: 28px; height: 28px; border-radius: 50%; background: var(--blue); flex: none; }

  /* back cover */
  .top-band { position: absolute; left: 0; top: 0; right: 0; height: 262px; background: var(--green); }
  .contact-panel {
    position: absolute; left: 118px; top: 72px; width: 258px; height: 360px; background: var(--blue);
    color: var(--white); text-align: center; padding-top: 34px;
  }
  .panel-lead { color: var(--green); font-size: 17px; line-height: 1.2; }
  .panel-phone { font-size: 24px; margin-top: 4px; }
  .panel-email-label { font-size: 14px; margin-top: 20px; }
  .panel-email { font-size: 12.5px; margin-top: 2px; }
  .panel-brand {
    position: absolute; left: 18px; bottom: 26px; display: flex; align-items: center; gap: 6px;
    font-size: 12px; line-height: 1.1; text-align: left;
  }
  .panel-brand .brand-dot { width: 22px; height: 22px; background: var(--white); }
  .panel-partner { position: absolute; right: 18px; bottom: 70px; font-size: 12px; line-height: 1.1; text-align: left; }
  .address-block { position: absolute; font-size: 8.5px; line-height: 1.35; color: var(--ink); font-style: normal; }
  .address-hq { left: 60px; top: 488px; }
  .address-holding { left: 282px; top: 446px; }
</style>
</head>
<body>

<section class="page front-cover">
  <div class="spine-bar"></div>
  <div class="spine-bar-accent"></div>
  <div class="spine-line"></div>
  <div class="side-band">
    <span class="band-green"></span><span class="band-light"></span><span class="band-mid"></span><span class="band-dark"></span>
  </div>
  <div class="hero-photo" role="img" aria-label="Sunlight through a forest canopy, seen looking up a tree trunk, cropped into a circle"></div>

  <div class="headline">
    <p class="headline-kicker">EVERYTHING</p>
    <h1 class="headline-main">ENERGY</h1>
  </div>

  <ul class="benefit-list">
    <li><svg viewBox="0 0 14 14"><circle cx="7" cy="7" r="6.5" fill="#9bcb3c"/><path d="M4 7.2l2 2 4-4.4" stroke="#fff" stroke-width="1.6" fill="none"/></svg>We manage pricing volatility.</li>
    <li><svg viewBox="0 0 14 14"><circle cx="7" cy="7" r="6.5" fill="#9bcb3c"/><path d="M4 7.2l2 2 4-4.4" stroke="#fff" stroke-width="1.6" fill="none"/></svg>We mitigate risk.</li>
    <li><svg viewBox="0 0 14 14"><circle cx="7" cy="7" r="6.5" fill="#9bcb3c"/><path d="M4 7.2l2 2 4-4.4" stroke="#fff" stroke-width="1.6" fill="none"/></svg>We secure the lowest cost.</li>
    <li><svg viewBox="0 0 14 14"><circle cx="7" cy="7" r="6.5" fill="#9bcb3c"/><path d="M4 7.2l2 2 4-4.4" stroke="#fff" stroke-width="1.6" fill="none"/></svg>We lower energy usage.</li>
    <li><svg viewBox="0 0 14 14"><circle cx="7" cy="7" r="6.5" fill="#9bcb3c"/><path d="M4 7.2l2 2 4-4.4" stroke="#fff" stroke-width="1.6" fill="none"/></svg>We reflect your energy values.</li>
  </ul>

  <p class="partner-name-front">Verdant Efficiency Group</p>
  <div class="brand-front"><span class="brand-dot"></span><span>Brightline<br>Power</span></div>
</section>

<section class="page back-cover">
  <div class="top-band"></div>
  <div class="contact-panel">
    <p class="panel-lead">Call today for a free energy<br>consultation:</p>
    <p class="panel-phone">312-555-0148</p>
    <p class="panel-email-label">Or email:</p>
    <p class="panel-email">savings@brightlinepower.com</p>
    <p class="panel-partner">Verdant<br>Efficiency<br>Group</p>
    <div class="panel-brand"><span class="brand-dot"></span><span>Brightline<br>Power</span></div>
  </div>

  <address class="address-block address-hq">
    ILLINOIS HEADQUARTERS<br>
    420 West Harbor Street<br>
    Suite 400<br>
    Chicago, IL 60654<br>
    800.555.0172<br>
    www.brightlinepower.com<br>
    www.verdantefficiency.com
  </address>
  <address class="address-block address-holding">
    SUMMIT CREST HOLDINGS<br>
    A Publicly Traded Energy Services<br>
    Company (SCHL)<br>
    275 Orchard Lane<br>
    Suite F<br>
    Irvine, CA 92618<br>
    (949) 555-0136
  </address>
</section>

</body>
</html>
```